Tavola coffee shop
Tavola Cafe'
To all designer : please try to make idea to add food items in the future which will not affect the design
All designer : i hope when we start the menu to start with the coffee section then juice section then........
All Designer , no need to stick to the same dimenssion that i gave u . you can prpose any dimenssion
Dear All
the Uploaded attachment is only an example and not to copy the same design
Dear all
My coffee shop logo is the arabic name and not the circle
to have good start, we need to show in our design the layout of the writing and not to copy the word format file and past it in the design. in addtion this boklet my be 4 page exluding the cover page
i need the menu to be as booklet
the size of the paper is 21.2cmX27.9cm

```html
<!DOCTYPE html>
<html lang="en">
<head>
<meta charset="utf-8">
<title>Tavola Cafe' — Menu Spread</title>
<link href="https://fonts.googleapis.com/css2?family=Arimo:wght@400;700&family=Cairo:wght@400;700&display=swap" rel="stylesheet">
<style>
  :root {
    --paper: #ffffff;
    --red: #d4161b;
    --red-deep: #8f0a0d;
    --red-mid: #b50f13;
    --gold: #f7c23c;
    --ink: #2a0a0a;
    --note: #5a2a2a;
    --cream: rgba(255, 245, 240, 0.9);
  }
  * { box-sizing: border-box; margin: 0; padding: 0; }
  html, body {
    width: 1200px; height: 473px; overflow: hidden;
    background: var(--paper);
    font-family: "Arimo", Arial, sans-serif;
  }
  .spread { position: relative; width: 1200px; height: 473px; }

  /* Cover */
  .cover {
    position: absolute; left: 6px; top: 6px; width: 582px; height: 461px;
    background: radial-gradient(ellipse at 62% 40%, #ee2a22 0%, var(--red) 45%, var(--red-mid) 80%, var(--red-deep) 100%);
    overflow: hidden;
  }
  .cover-floral {
    position: absolute; left: 0; top: 0; width: 330px; height: 300px;
    background: radial-gradient(ellipse at 35% 35%, rgba(255, 214, 90, 0.75) 0%, rgba(245, 150, 40, 0.45) 45%, rgba(212, 22, 27, 0) 75%);
  }
  .cover-brand {
    position: absolute; left: 260px; top: 360px;
    font-weight: 700; font-size: 40px; color: var(--gold);
    white-space: nowrap;
  }

  /* Menu page */
  .menu-page {
    position: absolute; left: 606px; top: 6px; width: 588px; height: 461px;
    background: linear-gradient(90deg, var(--red-mid) 0%, var(--red) 55%, #e0372c 80%, var(--red) 100%);
    overflow: hidden;
  }
  .page-brand {
    position: absolute; left: 30px; top: 12px;
    font-weight: 700; font-size: 20px; color: var(--gold);
    white-space: nowrap;
  }
  .menu-card {
    position: absolute; left: 34px; top: 40px; width: 500px; height: 268px;
    background: var(--cream);
  }
  .section { position: absolute; left: 0; width: 500px; height: 134px; }
  .section.coffee { top: 0; }
  .section.juice { top: 134px; }
  .section-photo {
    position: absolute; left: 12px; top: 28px; width: 72px; height: 76px;
  }
  .coffee .section-photo { background: linear-gradient(135deg, #e8c8a0 0%, #9a5a2a 55%, #4a2410 100%); }
  .juice .section-photo { background: linear-gradient(135deg, #fff0b8 0%, #f4a32a 50%, #d2561c 100%); }
  .section-title {
    position: absolute; left: 96px; top: 8px;
    font-weight: 700; font-size: 17px; color: var(--red);
    white-space: nowrap;
  }
  .section-title-ar {
    position: absolute; right: 14px; top: 2px;
    font-family: "Cairo", Arial, sans-serif; font-weight: 700; font-size: 16px; color: var(--red);
    direction: rtl; white-space: nowrap;
  }
  .items { position: absolute; left: 96px; top: 32px; width: 390px; list-style: none; }
  .item {
    position: relative; height: 18px;
    font-size: 11px; color: var(--ink); white-space: nowrap;
  }
  .item.with-note { height: 27px; }
  .item .name { position: absolute; left: 0; top: 0; font-weight: 700; }
  .item .note { position: absolute; left: 0; top: 13px; font-size: 7px; color: var(--note); }
  .item .price { position: absolute; left: 190px; top: 0; }
  .item .name-ar {
    position: absolute; right: 0; top: -3px;
    font-family: "Cairo", Arial, sans-serif; font-size: 11px; direction: rtl;
  }

  /* Photo strip */
  .photo-strip {
    position: absolute; left: 0; top: 318px; width: 588px; height: 143px;
    display: flex; gap: 4px; padding-left: 4px;
    background: var(--red-deep);
  }
  .strip-tile { flex: 1; height: 100%; }
  .strip-tile.t1 { background: linear-gradient(135deg, #e9c07a, #7a3a14); }
  .strip-tile.t2 { background: linear-gradient(135deg, #f5e3c0, #a8602a); }
  .strip-tile.t3 { background: linear-gradient(135deg, #ffe08a, #e87a1a); }
  .strip-tile.t4 { background: linear-gradient(135deg, #c98a4a, #4a2410); }
  .strip-tile.t5 { background: linear-gradient(135deg, #b7773e, #3e1c0c); }
</style>
</head>
<body>
<main class="spread">
  <section class="cover">
    <div class="cover-floral" role="img" aria-label="Golden floral ornament with white blossoms sweeping from the top left corner"></div>
    <div class="cover-brand">Tavola Cafe'</div>
  </section>

  <section class="menu-page">
    <div class="page-brand">Tavola Cafe'</div>

    <div class="menu-card">
      <div class="section coffee">
        <div class="section-photo" role="img" aria-label="Photo of a cup of hot coffee"></div>
        <h2 class="section-title">HOT COFFEE</h2>
        <h2 class="section-title-ar">القهوة الساخنة</h2>
        <ul class="items">
          <li class="item with-note">
            <span class="name">Espresso</span>
            <span class="note">Single or double shot of fresh roast</span>
            <span class="price">10rs.</span>
            <span class="name-ar">إسبريسو</span>
          </li>
          <li class="item"><span class="name">Cappuccino</span><span class="price">15rs.</span><span class="name-ar">كابتشينو</span></li>
          <li class="item"><span class="name">Caffe Latte</span><span class="price">15rs.</span><span class="name-ar">كافيه لاتيه</span></li>
          <li class="item"><span class="name">Turkish Coffee</span><span class="price">12rs.</span><span class="name-ar">قهوة تركية</span></li>
        </ul>
      </div>

      <div class="section juice">
        <div class="section-photo" role="img" aria-label="Photo of a glass of fresh juice"></div>
        <h2 class="section-title">FRESH JUICE</h2>
        <h2 class="section-title-ar">العصائر الطازجة</h2>
        <ul class="items">
          <li class="item"><span class="name">Orange</span><span class="price">12rs.</span><span class="name-ar">برتقال</span></li>
          <li class="item"><span class="name">Mango</span><span class="price">15rs.</span><span class="name-ar">مانجو</span></li>
          <li class="item"><span class="name">Strawberry</span><span class="price">15rs.</span><span class="name-ar">فراولة</span></li>
          <li class="item with-note">
            <span class="name">Lemon Mint</span>
            <span class="note">Freshly squeezed and served over crushed ice</span>
            <span class="price">12rs.</span>
            <span class="name-ar">ليمون بالنعناع</span>
          </li>
        </ul>
      </div>
    </div>

    <div class="photo-strip">
      <div class="strip-tile t1" role="img" aria-label="Photo of a latte with foam art"></div>
      <div class="strip-tile t2" role="img" aria-label="Photo of an iced coffee"></div>
      <div class="strip-tile t3" role="img" aria-label="Photo of fresh orange juice"></div>
      <div class="strip-tile t4" role="img" aria-label="Photo of baked pastries"></div>
      <div class="strip-tile t5" role="img" aria-label="Photo of roasted coffee beans"></div>
    </div>
  </section>
</main>
</body>
</html>
```